Meadow Hollow Beauty brand redesign of product labels

national rebrand of skincare product labels - same design but 6 sizes. Will be used for facial serums, body oils, bath salts, room sprays, etc. All labels to be same design - just adjusted for the different sizes. See brand document and sample label.

Bottle Specifications are located in the branding file.
Fonts included in product branding document.
Colours included in branding document.

Featuring company name and logo, product name, product feature, ingredients, size, directions, tag line. See attached sample label as example for design.

Black label base - matt.

Target Market(s)

Natural beauty, 20-60

Industry/Entity Type

farming, natural beauty

Font styles to use
Sans Serif

Requirements
Must have
• Modern, clean, homey
Nice to have
• modern clean design - using the branding colours provided
Should not have
• busy, crowded,

```html
<!DOCTYPE html>
<html lang="en">
<head>
<meta charset="utf-8">
<title>Meadow Hollow Beauty – Petalune Skin Repair Label</title>
<link href="https://fonts.googleapis.com/css2?family=Open+Sans:wght@300;400;600;700&family=Allura&display=swap" rel="stylesheet">
<style>
  :root {
    --label-black: #231f20;
    --mauve: #a89ea2;
    --cream: #f4ede4;
    --white: #ffffff;
    --page: #ffffff;
    --floral-rose: #e8a8a0;
    --floral-deep-rose: #c96a5f;
    --floral-teal: #6fa9a0;
    --floral-gold: #e7a63a;
  }
  * { margin: 0; padding: 0; box-sizing: border-box; }
  html, body {
    width: 1200px; height: 1200px; overflow: hidden;
    background: var(--page);
  }
  .canvas { position: relative; width: 1200px; height: 1200px; }
  .label {
    position: absolute; left: 60px; top: 330px;
    width: 1080px; height: 540px;
    background: var(--label-black);
    overflow: hidden;
    font-family: "Open Sans", sans-serif;
  }
  .floral { position: absolute; }
  .floral--top {
    left: 200px; top: 0; width: 310px; height: 250px;
    background: radial-gradient(ellipse 50% 50% at 50% 35%,
      rgba(232,168,160,0.95) 0%, rgba(201,106,95,0.85) 35%,
      rgba(111,169,160,0.6) 65%, rgba(35,31,32,0) 100%);
  }
  .floral--bottom {
    left: 594px; top: 291px; width: 486px; height: 249px;
    background: radial-gradient(ellipse 55% 60% at 70% 78%,
      rgba(243,208,200,0.95) 0%, rgba(232,168,160,0.9) 30%,
      rgba(111,169,160,0.7) 55%, rgba(231,166,58,0.45) 78%, rgba(35,31,32,0) 100%);
  }
  .brand {
    position: absolute; left: 0; top: 92px; width: 1080px;
    display: flex; justify-content: center; align-items: center; gap: 10px;
  }
  .brand__dot {
    width: 12px; height: 12px; border-radius: 50%;
    border: 1.5px solid var(--cream);
  }
  .brand__name {
    font-weight: 300; font-size: 16px; letter-spacing: 2px;
    color: var(--cream); text-transform: uppercase;
  }
  .tagline {
    position: absolute; left: 46px; top: 266px;
    transform: translate(-50%, -50%) rotate(-90deg);
    white-space: nowrap;
    font-weight: 300; font-size: 22px; letter-spacing: 1px;
    color: var(--mauve);
  }
  .product-name {
    position: absolute; left: 0; width: 1080px; top: 186px;
    text-align: center;
    font-family: "Allura", cursive; font-weight: 400;
    font-size: 96px; line-height: 1;
    color: var(--mauve);
  }
  .feature-band {
    position: absolute; left: 87px; top: 325px;
    width: 906px; height: 66px;
    background: var(--mauve);
    display: flex; align-items: center; justify-content: center;
  }
  .feature-band__text {
    text-align: center;
    font-weight: 700; font-size: 18px; line-height: 1.4;
    color: var(--cream);
  }
  .product-type {
    position: absolute; left: 0; width: 1080px; top: 401px;
    text-align: center; font-size: 25px; font-weight: 400;
    letter-spacing: 1px; color: var(--white);
  }
  .net-size {
    position: absolute; left: 0; width: 1080px; top: 494px;
    text-align: center; font-size: 12px; color: var(--cream);
  }
</style>
</head>
<body>
<main class="canvas">
  <section class="label">
    <div class="floral floral--top" role="img" aria-label="Watercolour bouquet of pink roses, blush blossoms, sunflower and green leaves"></div>

    <div class="brand">
      <span class="brand__dot"></span>
      <span class="brand__name">Meadow Hollow Beauty</span>
    </div>

    <p class="tagline">rooted in nature, grown with care</p>

    <h1 class="product-name">Petalune</h1>

    <div class="feature-band">
      <p class="feature-band__text">CONCENTRATED<br>HIALURONIC ACID GEL</p>
    </div>

    <div class="floral floral--bottom" role="img" aria-label="Watercolour bouquet of roses, blush blossoms, orange berries and foliage"></div>

    <p class="product-type">SKIN REPAIR</p>
    <p class="net-size">net 6,8 oz | 200 ml</p>
  </section>
</main>
</body>
</html>
```